Require stationery design which includes the following items as a minimum.

- Business card design
- Letterhead
- Envelopes

Details for business card:
Logo: Main logo is called "dove interiors square gold" but you may make use of whichever logo works best.
Tagline: Exquisite Furniture & Furnishings
Name: Helen Marchetti
Title: Interior Stylist
Mobile: 0432 871 264
PH: 03 9572 3140
Email: helen@dove-interiors.com.au

```html
<!DOCTYPE html>
<html lang="en">
<head>
<meta charset="utf-8">
<title>Dove Interiors – Business Card</title>
<link href="https://fonts.googleapis.com/css2?family=Arimo:wght@400;700&display=swap" rel="stylesheet">
<style>
  :root {
    --backdrop: #2a2c2e;
    --card-light: #a9afb1;
    --card-mid: #8f9597;
    --card-dark: #7d8385;
    --card-edge: rgba(235, 240, 242, 0.55);
    --gold: #d6c25a;
    --ink-white: #ffffff;
    --shadow-ink: rgba(40, 44, 46, 0.45);
  }
  * { margin: 0; padding: 0; box-sizing: border-box; }
  html, body {
    width: 1200px;
    height: 1000px;
    overflow: hidden;
    background: var(--backdrop);
    font-family: "Arimo", Arial, sans-serif;
  }
  .stage {
    position: relative;
    width: 1200px;
    height: 1000px;
  }
  .business-card {
    position: absolute;
    left: 150px;
    top: 220px;
    width: 900px;
    height: 560px;
    border-radius: 30px;
    background: linear-gradient(135deg, var(--card-light) 0%, var(--card-mid) 55%, var(--card-dark) 100%);
    box-shadow: inset 0 0 0 3px var(--card-edge), 0 20px 50px rgba(0, 0, 0, 0.45);
    overflow: hidden;
  }
  .brand {
    position: absolute;
    left: 150px;
    bottom: 50px;
    writing-mode: vertical-rl;
    transform: rotate(180deg);
    display: flex;
    align-items: center;
    gap: 18px;
  }
  .brand-mark {
    width: 44px;
    height: 44px;
    border-radius: 50%;
    background: var(--gold);
  }
  .brand-name {
    color: var(--gold);
    font-weight: 400;
    font-size: 36px;
    line-height: 1;
    letter-spacing: 4px;
    text-transform: uppercase;
    white-space: nowrap;
  }
  .contact {
    position: absolute;
    left: 330px;
    top: 170px;
    color: var(--ink-white);
  }
  .contact-name {
    font-weight: 700;
    font-size: 40px;
    text-shadow: 1px 2px 2px var(--shadow-ink);
  }
  .contact-title {
    margin-top: 6px;
    color: var(--gold);
    font-weight: 700;
    font-size: 18px;
  }
  .contact-list {
    margin-top: 14px;
    display: grid;
    grid-template-columns: 54px auto;
    row-gap: 14px;
    align-items: baseline;
  }
  .contact-label {
    color: var(--gold);
    font-weight: 700;
    font-size: 22px;
  }
  .contact-value {
    font-weight: 400;
    font-size: 28px;
    text-shadow: 1px 2px 2px var(--shadow-ink);
  }
  .contact-value.is-phone { padding-left: 30px; }
</style>
</head>
<body>
  <main class="stage">
    <article class="business-card">
      <div class="brand">
        <span class="brand-mark"></span>
        <span class="brand-name">Dove Interiors</span>
      </div>
      <section class="contact">
        <h1 class="contact-name">Helen Marchetti</h1>
        <p class="contact-title">Interior Stylist</p>
        <dl class="contact-list">
          <dt class="contact-label">T:</dt>
          <dd class="contact-value is-phone">0432 871 264</dd>
          <dt class="contact-label">PH:</dt>
          <dd class="contact-value is-phone">03 9572 3140</dd>
          <dt class="contact-label">E:</dt>
          <dd class="contact-value">helen@dove-interiors.com.au</dd>
        </dl>
      </section>
    </article>
  </main>
</body>
</html>
```